QTR Business Card

Harborline Capital Partners is a successful and reputable financial services company.Our main services are home loans, commercial loans, vehicle finance and equipment finance. We also do development finance for property developers. Our company is always evolving to always be an industry leader in best financial service practices with access to the largest range of lenders in the country.

We want the business card to reflect our national finance company. Modern, professional corporate image. At the same time the concept of Harborline Capital Partners is that we help build wealth for you but the process for the client is an enjoyable peaceful experience. Not stressful at all .....

Colors to be same as the logo .... gold silver black white as the options

On the reverse side of the card I wanted either just the logo symbol or the logo symbol and text of the logo ....

It could be on a black background ..... or silver or gold .... want it to be quite striking to look at when you first see the card.

On the other side of the card I wanted the following details:

Doran Pelham
Director

0498 372 604

doran@hbcpx.com.au

Po Box 852
Tarrow ACT 2694

www.hbcpx.com.au

ACN 918 264 057 (This can be in very small print and can be in the bottom corner of the card or somewhere not very prominent)
Updates

As requested Ive uploaded the logo file in both .ai and .pdf formats. Please let me know if you need anything else. Thanks

Reason: Still deciding on which design I like best. I will provide individual feedback as well.

```html
<!DOCTYPE html>
<html lang="en">
<head>
<meta charset="utf-8">
<title>QTR Business Card</title>
<link rel="stylesheet" href="https://fonts.googleapis.com/css2?family=Noto+Serif:wght@400;600;700&display=swap">
<style>
  :root {
    --stage: #d9d9da;
    --card: #2b2b2c;
    --card-deep: #1c1c1d;
    --band: #3b3b3d;
    --gold: #d9a921;
    --gold-light: #f6d23a;
    --gold-dark: #b07d14;
    --silver: #a9a9ab;
    --silver-dim: #8d8d90;
  }
  * { box-sizing: border-box; margin: 0; padding: 0; }
  html, body { width: 1200px; height: 926px; overflow: hidden; }
  body {
    background: var(--stage);
    font-family: "Noto Serif", Georgia, serif;
    position: relative;
  }
  .card {
    position: absolute;
    left: 280px;
    width: 640px;
    height: 391px;
    background: var(--card);
    border-radius: 4px;
    overflow: hidden;
    box-shadow: 0 6px 18px rgba(0,0,0,0.18);
  }
  .card--back { top: 48px; }
  .card--front { top: 487px; }

  .brand { display: flex; align-items: center; gap: 14px; }
  .brand__dot {
    border-radius: 50%;
    background: var(--gold);
    flex: none;
  }
  .brand__name {
    color: var(--gold);
    font-weight: 600;
    line-height: 1.1;
    letter-spacing: 0.04em;
  }
  .brand__name span { display: block; }

  .card--back .brand {
    position: absolute;
    left: 50%; top: 50%;
    transform: translate(-50%, -50%);
  }
  .card--back .brand__dot { width: 78px; height: 78px; }
  .card--back .brand__name { font-size: 30px; }
  .card--back .brand__name .brand__sub { font-size: 14px; letter-spacing: 0.22em; margin-top: 4px; }

  .card--front .brand { position: absolute; left: 40px; top: 32px; gap: 12px; }
  .card--front .brand__dot { width: 50px; height: 50px; }
  .card--front .brand__name { font-size: 20px; }
  .card--front .brand__name .brand__sub { font-size: 9px; letter-spacing: 0.2em; margin-top: 3px; }

  .person { position: absolute; left: 40px; top: 102px; }
  .person__name { color: var(--gold); font-size: 24px; font-weight: 400; }
  .person__name strong { font-weight: 700; }
  .person__role { color: var(--silver-dim); font-size: 14px; margin-top: 2px; }

  .waves { position: absolute; inset: 0; width: 640px; height: 391px; }

  .contact {
    position: absolute;
    right: 36px; top: 160px;
    list-style: none;
    text-align: right;
  }
  .contact li {
    display: flex;
    justify-content: flex-end;
    align-items: center;
    gap: 12px;
    color: var(--silver);
    font-size: 17px;
    height: 28px;
  }
  .contact svg { width: 18px; height: 18px; flex: none; fill: var(--gold); }

  .acn {
    position: absolute;
    left: 40px; bottom: 40px;
    color: var(--silver);
    font-size: 14px;
    font-weight: 600;
    letter-spacing: 0.03em;
  }
</style>
</head>
<body>

<section class="card card--back" aria-label="Card reverse">
  <div class="brand">
    <div class="brand__dot"></div>
    <div class="brand__name">
      <span>Harborline</span>
      <span class="brand__sub">Capital Partners</span>
    </div>
  </div>
</section>

<section class="card card--front" aria-label="Card front">
  <svg class="waves" viewBox="0 0 640 391" aria-hidden="true">
    <defs>
      <linearGradient id="goldRibbon" x1="0" y1="0" x2="1" y2="0">
        <stop offset="0" stop-color="var(--gold-dark)"/>
        <stop offset="0.35" stop-color="var(--gold-light)"/>
        <stop offset="0.7" stop-color="var(--gold)"/>
        <stop offset="1" stop-color="var(--gold-dark)"/>
      </linearGradient>
    </defs>
    <path d="M0,250 C150,228 300,248 420,300 C520,340 600,352 640,356 L640,391 L0,391 Z" fill="var(--band)"/>
    <path d="M0,280 C140,262 260,272 380,320 C470,356 560,378 640,376 L640,391 L0,391 Z" fill="url(#goldRibbon)"/>
    <path d="M0,290 C150,276 270,292 380,338 C460,372 540,391 600,391 L0,391 Z" fill="var(--card-deep)"/>
  </svg>

  <div class="brand">
    <div class="brand__dot"></div>
    <div class="brand__name">
      <span>Harborline</span>
      <span class="brand__sub">Capital Partners</span>
    </div>
  </div>

  <div class="person">
    <h1 class="person__name"><strong>Doran</strong> Pelham</h1>
    <p class="person__role">Director</p>
  </div>

  <ul class="contact">
    <li>0498 372 604
      <svg viewBox="0 0 24 24"><path d="M7 1h10a2 2 0 0 1 2 2v18a2 2 0 0 1-2 2H7a2 2 0 0 1-2-2V3a2 2 0 0 1 2-2zm0 3v12h10V4zm5 14a1.5 1.5 0 1 0 0 3a1.5 1.5 0 0 0 0-3z"/></svg>
    </li>
    <li>www.hbcpx.com.au
      <svg viewBox="0 0 24 24"><path d="M12 1a11 11 0 1 0 0 22a11 11 0 0 0 0-22zm0 2c1.4 1.4 2.4 3.5 2.8 6H9.2C9.6 6.5 10.6 4.4 12 3zM8.9 3.6A13 13 0 0 0 7.2 9H3.6a9 9 0 0 1 5.3-5.4zm6.2 0A9 9 0 0 1 20.4 9h-3.6a13 13 0 0 0-1.7-5.4zM3.2 11h3.9a17 17 0 0 0 0 2H3.2a9 9 0 0 1 0-2zm5.9 0h5.8a15 15 0 0 1 0 2H9.1a15 15 0 0 1 0-2zm7.8 0h3.9a9 9 0 0 1 0 2h-3.9a17 17 0 0 0 0-2zM3.6 15h3.6a13 13 0 0 0 1.7 5.4A9 9 0 0 1 3.6 15zm5.6 0h5.6c-.4 2.5-1.4 4.6-2.8 6c-1.4-1.4-2.4-3.5-2.8-6zm7.6 0h3.6a9 9 0 0 1-5.3 5.4a13 13 0 0 0 1.7-5.4z"/></svg>
    </li>
    <li>doran@hbcpx.com.au
      <svg viewBox="0 0 24 24"><path d="M2 5h20v14H2zm2 2v.4l8 5.2l8-5.2V7zm0 2.8V17h16V9.8l-8 5.2z"/></svg>
    </li>
    <li>Po Box 852 Tarrow ACT 2694
      <svg viewBox="0 0 24 24"><path d="M12 1a8 8 0 0 0-8 8c0 6 8 14 8 14s8-8 8-14a8 8 0 0 0-8-8zm0 5a3 3 0 1 1 0 6a3 3 0 0 1 0-6z"/></svg>
    </li>
  </ul>

  <p class="acn">ACN 918 264 057</p>
</section>

</body>
</html>
```